Information Security Company Business Cards

Using our included logo, we need a business card design. It should have standard contact information such as :

Ravi Kunst
Senior Security Engineer
ravi.kunst@brindale-works.com
866.555.0193

Maybe include the website "www.brindale-works.com" that we will be redesigning soon.??

open to suggestions of course...

Target Market(s)

Our customers are small to large companies. Generally health-care, financial, insurance and the like.

Industry/Entity Type

Business

Font styles to use
Other font styles liked:
• Something that works with the logo

Requirements
Must have
• Colors should flow with the logo if possible. Or at least we think it should.

```html
<!DOCTYPE html>
<html lang="en">
<head>
<meta charset="utf-8">
<title>Brindale Works Business Cards</title>
<link href="https://fonts.googleapis.com/css2?family=Exo+2:wght@400;500;700&display=swap" rel="stylesheet">
<style>
  :root {
    --page-bg: #e4e4e6;
    --brand-blue: #3a3f98;
    --brand-blue-deep: #2c3186;
    --brand-blue-light: #474c9f;
    --ink-dark: #3a3a3c;
    --paper: #ffffff;
    --text-on-blue: #ffffff;
    --shadow: rgba(0, 0, 0, 0.22);
  }
  * { box-sizing: border-box; margin: 0; padding: 0; }
  html, body {
    width: 1200px;
    height: 914px;
    overflow: hidden;
    background: var(--page-bg);
    font-family: "Exo 2", sans-serif;
  }
  .sheet {
    position: relative;
    width: 1200px;
    height: 914px;
  }
  .card {
    position: absolute;
    width: 700px;
    height: 400px;
    overflow: hidden;
    box-shadow: 0 14px 30px var(--shadow);
  }
  /* Back of card */
  .card-back {
    left: 420px;
    top: 48px;
    background: linear-gradient(135deg, var(--brand-blue-light), var(--brand-blue-deep));
    display: flex;
    align-items: center;
    justify-content: center;
  }
  .brand {
    display: flex;
    align-items: center;
    gap: 18px;
  }
  .brand-dot {
    border-radius: 50%;
    flex: none;
  }
  .card-back .brand-dot {
    width: 58px;
    height: 58px;
    border: 6px solid var(--text-on-blue);
  }
  .card-back .brand-name {
    color: var(--text-on-blue);
    font-weight: 700;
    font-size: 44px;
    letter-spacing: 2px;
    text-transform: uppercase;
  }
  /* Front of card */
  .card-front {
    left: 80px;
    top: 478px;
    display: flex;
    background: var(--paper);
  }
  .front-brand-panel {
    width: 275px;
    height: 100%;
    background: var(--paper);
    display: flex;
    align-items: center;
    justify-content: center;
  }
  .front-brand-panel .brand {
    flex-direction: column;
    gap: 16px;
  }
  .front-brand-panel .brand-dot {
    width: 90px;
    height: 90px;
    border: 9px solid var(--brand-blue);
  }
  .front-brand-panel .brand-name {
    color: var(--brand-blue);
    font-weight: 700;
    font-size: 30px;
    letter-spacing: 1.5px;
    text-transform: uppercase;
    text-align: center;
    line-height: 1.05;
  }
  .divider {
    width: 6px;
    height: 100%;
    background: linear-gradient(to right, var(--brand-blue) 0 2px, var(--paper) 2px 4px, var(--brand-blue) 4px);
  }
  .front-contact-panel {
    flex: 1;
    height: 100%;
    background: linear-gradient(135deg, var(--brand-blue-light), var(--brand-blue-deep));
    color: var(--text-on-blue);
    padding: 95px 0 0 60px;
  }
  .person-name {
    font-size: 30px;
    font-weight: 500;
    letter-spacing: 1.5px;
  }
  .person-title {
    font-size: 16px;
    font-weight: 400;
    letter-spacing: 1px;
    margin-top: 2px;
    margin-bottom: 32px;
    padding-left: 4px;
  }
  .contact-list { list-style: none; }
  .contact-item {
    display: flex;
    align-items: center;
    gap: 18px;
    font-size: 19px;
    letter-spacing: 1.2px;
    margin-bottom: 12px;
  }
  .contact-icon {
    width: 22px;
    height: 18px;
    flex: none;
  }
</style>
</head>
<body>
<main class="sheet">
  <section class="card card-back" aria-label="Card back">
    <div class="brand">
      <span class="brand-dot"></span>
      <span class="brand-name">Brindale Works</span>
    </div>
  </section>

  <section class="card card-front" aria-label="Card front">
    <div class="front-brand-panel">
      <div class="brand">
        <span class="brand-dot"></span>
        <span class="brand-name">Brindale<br>Works</span>
      </div>
    </div>
    <div class="divider"></div>
    <div class="front-contact-panel">
      <h1 class="person-name">Ravi Kunst</h1>
      <p class="person-title">Senior Security Engineer</p>
      <ul class="contact-list">
        <li class="contact-item">
          <svg class="contact-icon" viewBox="0 0 22 18" aria-hidden="true">
            <path d="M2 6 Q11 0 20 6 L17 8 L15 5 L7 5 L5 8 Z" fill="#fff"/>
            <rect x="4" y="9" width="14" height="8" rx="1" fill="#fff"/>
          </svg>
          <span>866.555.0193</span>
        </li>
        <li class="contact-item">
          <svg class="contact-icon" viewBox="0 0 22 18" aria-hidden="true">
            <rect x="1" y="2" width="20" height="14" fill="none" stroke="#fff" stroke-width="2"/>
            <path d="M1 2 L11 10 L21 2" fill="none" stroke="#fff" stroke-width="2"/>
          </svg>
          <span>ravi.kunst@brindale-works.com</span>
        </li>
        <li class="contact-item">
          <svg class="contact-icon" viewBox="0 0 22 18" aria-hidden="true">
            <rect x="1" y="1" width="20" height="12" fill="none" stroke="#fff" stroke-width="2"/>
            <rect x="9" y="13" width="4" height="3" fill="#fff"/>
            <rect x="6" y="16" width="10" height="2" fill="#fff"/>
          </svg>
          <span>www.brindale-works.com</span>
        </li>
      </ul>
    </div>
  </section>
</main>
</body>
</html>
```